Icons for each step of my seven step process

Hi, I run a business coaching service for dentists. I have a 7 step process I take my clients through. I need to create an icon for each of my steps.
I also need to create an info graphic that relates these 7 steps in a process ie one leading to the other and then ending up back at the beginning.
I'm also looking to possibly add an 8th step and would like an icon for that too as well as an info graphic showing the 8 steps please.
From a style point of view I like the look of BrellowNotes.com. My website will be clean looking and I'd like the icons to be clean looking as well. I'm happy for an array of colours to be used as well. I DO NOT want any icons with teeth or dental specific images. These icons should describe the process not the market.
I'd like the icon enclosed. I do like the rounded corners type of design often associated with apps but I'm open to other shapes as well.
I'd like the icons to have a professional feel but still look "cool and groovy"
The icons should not be numbered either please.
The seven / eight steps are:
1. Foundations
2. Building a high performance team
3. Operating Systems
4. Financial Systems
5. Case Acceptance (this is essentially a sales process - no shopping cart icons though please)
6. WOW customer service
7. Marketing
8. Creating Balance (not a yin yang please)
I'm happy if you need to abbreviate some of these points to a single word or two EG Team.
Many thanks,
Corin
Target Market(s)
Dentists
Industry/Entity Type
Shopping
Requirements
Must have
- Enclosed images for the icons but not necessarily for the infogrpahic.
Professional looking but still look cool / arty / groovy
Modern font.
Nice to have
- See BrellowNotes.com for inspiration.
Should not have
- No illustrations of "shopping carts" for case acceptance and no illustrations of "yin yang's" for balance.
No old style fancy / flowery fonts.
No metallic type or reflective icons please.

```html
<!DOCTYPE html>
<html lang="en">
<head>
<meta charset="utf-8">
<title>Clinic Momentum – Eight Step Cycle</title>
<link rel="stylesheet" href="https://fonts.googleapis.com/css2?family=Open+Sans:wght@400;600&display=swap">
<style>
  :root {
    --step-foundations: #39b4df;
    --step-team: #8dc63f;
    --step-financial: #f7941d;
    --step-operating: #a5673b;
    --step-acceptance: #4f5052;
    --step-service: #ec2a8c;
    --step-marketing: #e1262c;
    --step-balance: #92278f;
    --title-red: #d9262c;
    --icon-white: #ffffff;
    --page: #ffffff;
  }
  html, body {
    margin: 0;
    padding: 0;
    width: 1200px;
    height: 605px;
    overflow: hidden;
    background: var(--page);
  }
  .cycle-board {
    display: block;
    width: 1200px;
    height: 605px;
  }
  .step-label {
    font-family: "Open Sans", Arial, sans-serif;
    font-size: 11.5px;
    fill: var(--icon-white);
    text-anchor: middle;
  }
  .step-label--lead { font-size: 13px; }
  .cycle-title {
    font-family: "Open Sans", Arial, sans-serif;
    font-weight: 400;
    fill: var(--title-red);
    text-anchor: middle;
  }
  .seg { stroke-linejoin: round; stroke-width: 6; }
  .seg--foundations { fill: var(--step-foundations); stroke: var(--step-foundations); }
  .seg--team { fill: var(--step-team); stroke: var(--step-team); }
  .seg--financial { fill: var(--step-financial); stroke: var(--step-financial); }
  .seg--operating { fill: var(--step-operating); stroke: var(--step-operating); }
  .seg--acceptance { fill: var(--step-acceptance); stroke: var(--step-acceptance); }
  .seg--service { fill: var(--step-service); stroke: var(--step-service); }
  .seg--marketing { fill: var(--step-marketing); stroke: var(--step-marketing); }
  .seg--balance { fill: var(--step-balance); stroke: var(--step-balance); }
  .seg-sheen { fill: url(#sheen); stroke: none; }
</style>
</head>
<body>
<svg class="cycle-board" viewBox="0 0 1200 605" xmlns="http://www.w3.org/2000/svg" role="img" aria-label="Clinic Momentum eight step cycle">
  <defs>
    <path id="segment" d="M 274.5 -108.1 A 295 295 0 0 1 274.5 108.1 L 203.9 110.7 L 158.2 62.3 A 170 170 0 0 0 158.2 -62.3 L 224.6 -58.1 Z"/>
    <linearGradient id="sheen" gradientUnits="userSpaceOnUse" x1="160" y1="-110" x2="290" y2="110">
      <stop offset="0" stop-color="#ffffff" stop-opacity="0.22"/>
      <stop offset="0.6" stop-color="#ffffff" stop-opacity="0"/>
      <stop offset="1" stop-color="#000000" stop-opacity="0.08"/>
    </linearGradient>

    <symbol id="icon-bank" viewBox="0 0 100 100">
      <g fill="#fff">
        <polygon points="50,8 94,30 6,30"/>
        <rect x="8" y="33" width="84" height="6"/>
        <rect x="16" y="43" width="9" height="34"/>
        <rect x="33" y="43" width="9" height="34"/>
        <rect x="58" y="43" width="9" height="34"/>
        <rect x="75" y="43" width="9" height="34"/>
        <rect x="8" y="80" width="84" height="5"/>
        <rect x="3" y="88" width="94" height="6"/>
      </g>
    </symbol>

    <symbol id="icon-team" viewBox="0 0 100 100">
      <g fill="#fff">
        <circle cx="36" cy="28" r="17"/>
        <path d="M6 78 C6 55 18 48 36 48 C54 48 64 55 64 78 Z"/>
      </g>
      <g fill="#fff" stroke="#8dc63f" stroke-width="3">
        <circle cx="64" cy="44" r="17"/>
        <path d="M34 96 C34 72 46 64 64 64 C82 64 94 72 94 96 Z"/>
      </g>
    </symbol>

    <symbol id="icon-coins" viewBox="0 0 100 100">
      <g fill="#fff" stroke="#f7941d" stroke-width="2.5">
        <ellipse cx="28" cy="86" rx="20" ry="7"/>
        <ellipse cx="28" cy="78" rx="20" ry="7"/>
        <ellipse cx="28" cy="70" rx="20" ry="7"/>
        <ellipse cx="28" cy="62" rx="20" ry="7"/>
        <ellipse cx="58" cy="80" rx="20" ry="7"/>
        <ellipse cx="58" cy="72" rx="20" ry="7"/>
        <ellipse cx="58" cy="64" rx="20" ry="7"/>
        <ellipse cx="58" cy="56" rx="20" ry="7"/>
        <ellipse cx="58" cy="48" rx="20" ry="7"/>
        <ellipse cx="58" cy="40" rx="20" ry="7"/>
        <ellipse cx="58" cy="32" rx="20" ry="7"/>
        <ellipse cx="58" cy="24" rx="20" ry="7"/>
        <ellipse cx="80" cy="86" rx="18" ry="6.5"/>
        <ellipse cx="80" cy="78" rx="18" ry="6.5"/>
        <ellipse cx="80" cy="70" rx="18" ry="6.5"/>
        <ellipse cx="80" cy="62" rx="18" ry="6.5"/>
        <ellipse cx="80" cy="54" rx="18" ry="6.5"/>
      </g>
    </symbol>

    <symbol id="icon-gears" viewBox="0 0 100 100">
      <g fill="none" stroke="#fff">
        <circle cx="34" cy="58" r="24" stroke-width="10" stroke-dasharray="9.4 9.4"/>
        <circle cx="72" cy="32" r="15" stroke-width="8" stroke-dasharray="6.6 5.2"/>
      </g>
      <g fill="#fff">
        <circle cx="34" cy="58" r="22"/>
        <circle cx="72" cy="32" r="13"/>
      </g>
      <g fill="#a5673b">
        <circle cx="34" cy="58" r="8"/>
        <circle cx="72" cy="32" r="5"/>
      </g>
    </symbol>

    <symbol id="icon-tick" viewBox="0 0 100 100">
      <circle cx="50" cy="50" r="42" fill="none" stroke="#fff" stroke-width="7"/>
      <polyline points="30,52 44,66 72,36" fill="none" stroke="#fff" stroke-width="9" stroke-linecap="round" stroke-linejoin="round"/>
    </symbol>

    <symbol id="icon-wow" viewBox="0 0 100 80">
      <path d="M50 4 C76 4 96 16 96 32 C96 48 76 60 50 60 C44 60 39 59 34 58 L16 74 L20 54 C10 49 4 41 4 32 C4 16 24 4 50 4 Z" fill="#fff"/>
      <text x="50" y="41" font-family="Open Sans, Arial, sans-serif" font-weight="600" font-size="26" fill="#ec2a8c" text-anchor="middle">WOW</text>
    </symbol>

    <symbol id="icon-target" viewBox="0 0 100 100">
      <circle cx="40" cy="58" r="36" fill="#fff"/>
      <circle cx="40" cy="58" r="30" fill="#e1262c"/>
      <circle cx="40" cy="58" r="23" fill="#fff"/>
      <circle cx="40" cy="58" r="16" fill="#e1262c"/>
      <circle cx="40" cy="58" r="9" fill="#fff"/>
      <circle cx="40" cy="58" r="4" fill="#e1262c"/>
      <line x1="42" y1="56" x2="86" y2="22" stroke="#3a3a3a" stroke-width="3.5" stroke-linecap="round"/>
      <polygon points="80,16 96,10 90,26 84,28 78,22" fill="#3a3a3a"/>
    </symbol>

    <symbol id="icon-scales" viewBox="0 0 100 100">
      <g fill="#fff" stroke="#fff">
        <rect x="47.5" y="10" width="5" height="74" stroke="none"/>
        <circle cx="50" cy="10" r="5" stroke="none"/>
        <rect x="12" y="20" width="76" height="4" stroke="none"/>
        <path d="M32 90 Q50 80 68 90 Z" stroke="none"/>
        <g fill="none" stroke-width="1.8">
          <polyline points="4,58 16,24 28,58"/>
          <polyline points="72,58 84,24 96,58"/>
        </g>
        <path d="M2 58 H30 Q16 74 2 58 Z" stroke="none"/>
        <path d="M70 58 H98 Q84 74 70 58 Z" stroke="none"/>
      </g>
    </symbol>
  </defs>

  <g class="cycle cycle--labelled">
    <g class="ring" transform="translate(300 303)">
      <g transform="rotate(-86)"><use href="#segment" class="seg seg--foundations"/><use href="#segment" class="seg-sheen"/></g>
      <g transform="rotate(-41)"><use href="#segment" class="seg seg--team"/><use href="#segment" class="seg-sheen"/></g>
      <g transform="rotate(4)"><use href="#segment" class="seg seg--financial"/><use href="#segment" class="seg-sheen"/></g>
      <g transform="rotate(49)"><use href="#segment" class="seg seg--operating"/><use href="#segment" class="seg-sheen"/></g>
      <g transform="rotate(94)"><use href="#segment" class="seg seg--acceptance"/><use href="#segment" class="seg-sheen"/></g>
      <g transform="rotate(139)"><use href="#segment" class="seg seg--service"/><use href="#segment" class="seg-sheen"/></g>
      <g transform="rotate(184)"><use href="#segment" class="seg seg--marketing"/><use href="#segment" class="seg-sheen"/></g>
      <g transform="rotate(229)"><use href="#segment" class="seg seg--balance"/><use href="#segment" class="seg-sheen"/></g>
    </g>

    <g class="step-icons">
      <use href="#icon-bank" x="262" y="38" width="76" height="66"/>
      <use href="#icon-team" x="432" y="104" width="56" height="56"/>
      <use href="#icon-coins" x="478" y="268" width="72" height="60"/>
      <use href="#icon-gears" x="400" y="426" width="80" height="64"/>
      <use href="#icon-tick" x="256" y="488" width="66" height="66"/>
      <use href="#icon-wow" x="92" y="420" width="66" height="54"/>
      <use href="#icon-target" x="28" y="248" width="76" height="76"/>
      <use href="#icon-scales" x="100" y="94" width="72" height="64"/>
    </g>

    <g class="step-labels">
      <text class="step-label step-label--lead" x="300" y="121">1. Foundations</text>
      <text class="step-label" x="480" y="174">2.Building a High</text>
      <text class="step-label" x="480" y="188">Performance Team</text>
      <text class="step-label" x="518" y="345">3. Financial Systems</text>
      <text class="step-label" x="443" y="506">4. Operating Systems</text>
      <text class="step-label" x="290" y="579">5. Case Acceptance</text>
      <text class="step-label" x="123" y="491">6. WOW Customer</text>
      <text class="step-label" x="123" y="505">Service</text>
      <text class="step-label" x="65" y="339">7. Marketing</text>
      <text class="step-label" x="140" y="168">8. Creating Balance</text>
    </g>

    <text class="cycle-title" x="290" y="287" font-size="44">Clinic</text>
    <text class="cycle-title" x="290" y="347" font-size="44">Momentum</text>
  </g>

  <g class="cycle cycle--icons">
    <g class="ring" transform="translate(905 300)">
      <g transform="rotate(-86)"><use href="#segment" class="seg seg--foundations"/><use href="#segment" class="seg-sheen"/></g>
      <g transform="rotate(-41)"><use href="#segment" class="seg seg--team"/><use href="#segment" class="seg-sheen"/></g>
      <g transform="rotate(4)"><use href="#segment" class="seg seg--financial"/><use href="#segment" class="seg-sheen"/></g>
      <g transform="rotate(49)"><use href="#segment" class="seg seg--operating"/><use href="#segment" class="seg-sheen"/></g>
      <g transform="rotate(94)"><use href="#segment" class="seg seg--acceptance"/><use href="#segment" class="seg-sheen"/></g>
      <g transform="rotate(139)"><use href="#segment" class="seg seg--service"/><use href="#segment" class="seg-sheen"/></g>
      <g transform="rotate(184)"><use href="#segment" class="seg seg--marketing"/><use href="#segment" class="seg-sheen"/></g>
      <g transform="rotate(229)"><use href="#segment" class="seg seg--balance"/><use href="#segment" class="seg-sheen"/></g>
    </g>

    <g class="step-icons">
      <use href="#icon-bank" x="858" y="18" width="94" height="82"/>
      <use href="#icon-team" x="1022" y="84" width="86" height="86"/>
      <use href="#icon-coins" x="1074" y="262" width="96" height="80"/>
      <use href="#icon-gears" x="998" y="420" width="104" height="84"/>
      <use href="#icon-tick" x="842" y="478" width="86" height="86"/>
      <use href="#icon-wow" x="688" y="406" width="88" height="72"/>
      <use href="#icon-target" x="626" y="240" width="96" height="96"/>
      <use href="#icon-scales" x="694" y="78" width="96" height="86"/>
    </g>

    <text class="cycle-title" x="897" y="276" font-size="46">Clinic</text>
    <text class="cycle-title" x="897" y="338" font-size="46">Momentum</text>
  </g>
</svg>
</body>
</html>
```